Marketing Flyer for Office Space for Lease

I am looking for a pretty standard and professional real estate flyer listing my property for lease. I am not looking for anything over the top creative, just something very professional looking. The building address is 4867 W. Tamberlin Avenue, Lauderhill, FL 33319. I included some sample flyers of what other companies use as examples on what I am looking for. Please use the attached Ordell Holdings Realty logo, but remove the long line after it extends past the words. I also included a Word file that gives you the building information and marketing information. Please use the photos attached in the zipped folder as you see fit.
Updates

Project Deadline Extended
Reason: I am getting updated building measurements next Thursday. I want to be able to give these figures to you to ensure the flyer is final. I will keep making comments on the rest of the designs while I wait for those numbers. Thank you.

Project Deadline Extended
Reason: Just got the floor plans, so I needed to adjust the figures on the flyer. Otherwise I would just have an incorrect flyer.

Target Market(s)

Businesses that would want to lease space in this building.

Industry/Entity Type

Real Estate

Font styles to use
Serif
Sans Serif

Colors

Designer to choose colors to be used in the design.

Requirements
Must have
• Building photo, address, map, and building highlights from the Word file.
Nice to have
• I included the example flyers that I have seen or used in the past. Taking ideas from there could work well.
Should not have
• Crazy big fonts, crazy colors, hard to read fonts, too wild of layout.

```html
<!DOCTYPE html>
<html lang="en">
<head>
<meta charset="utf-8">
<title>Office Space for Lease – 4867 W. Tamberlin Avenue</title>
<link rel="stylesheet" href="https://fonts.googleapis.com/css2?family=Figtree:wght@400;500;700&family=Montserrat:wght@500;700;800&display=swap">
<style>
  :root {
    --blue-deep: #145a9b;
    --blue-light: #5fa6d1;
    --ink: #111111;
    --paper: #ffffff;
    --photo-sky: #b9d3ea;
    --photo-wall: #e6e9ec;
    --photo-lot: #6f7378;
    --map-fill: #eceef0;
    --map-border: #9aa3ab;
  }
  * { box-sizing: border-box; margin: 0; padding: 0; }
  html, body { width: 927px; height: 1200px; overflow: hidden; background: var(--paper); }
  body { font-family: "Figtree", Arial, sans-serif; color: var(--ink); position: relative; }

  .band {
    position: absolute;
    background: linear-gradient(90deg, var(--blue-deep) 0%, var(--blue-light) 50%, var(--blue-deep) 100%);
    color: var(--paper);
    font-family: "Montserrat", Arial, sans-serif;
  }
  .band--title { left: 17px; top: 26px; width: 893px; height: 67px; display: flex; align-items: center; justify-content: center; }
  .band--title h1 { font-weight: 800; font-size: 41px; letter-spacing: 0.3px; }

  .address { position: absolute; left: 0; top: 107px; width: 927px; text-align: center; font-family: "Montserrat", Arial, sans-serif; font-weight: 700; font-size: 27px; }

  .photo { position: absolute; }
  .photo--main { left: 26px; top: 156px; width: 549px; height: 390px;
    background: linear-gradient(180deg, var(--photo-sky) 0%, var(--photo-wall) 45%, var(--photo-wall) 68%, var(--photo-lot) 100%); }
  .photo--aerial { left: 582px; top: 307px; width: 315px; height: 186px;
    background: linear-gradient(160deg, #8fb07a 0%, var(--photo-wall) 45%, var(--photo-lot) 100%); }
  .photo--street { left: 582px; top: 502px; width: 315px; height: 98px;
    background: linear-gradient(180deg, var(--photo-sky) 0%, var(--photo-wall) 55%, #7f9c6a 100%); }

  .band--section { display: flex; align-items: center; font-weight: 800; font-size: 15.5px; }
  .band--info { left: 582px; top: 156px; width: 315px; height: 50px; padding-left: 9px; }
  .band--marketing { left: 26px; top: 552px; width: 549px; height: 48px; padding-left: 35px; }

  .arrow { display: inline-block; width: 0; height: 0; border-top: 5px solid transparent; border-bottom: 5px solid transparent; border-left: 9px solid var(--ink); flex: none; }

  .facts { position: absolute; left: 598px; top: 218px; list-style: none; font-size: 15px; }
  .facts li { display: flex; align-items: center; gap: 9px; height: 27px; }
  .facts b { font-weight: 700; }
  .facts sup { font-size: 9px; }

  .features { position: absolute; left: 68px; top: 616px; width: 500px; list-style: none; font-size: 15px; line-height: 19px; }
  .features > li { display: flex; gap: 15px; margin-bottom: 7px; }
  .features > li > .arrow { margin-top: 5px; }
  .features .sub { list-style: none; margin-top: 5px; margin-left: 41px; }
  .features .sub li { display: flex; align-items: center; gap: 10px; height: 20.6px; }

  .map { position: absolute; left: 582px; top: 607px; width: 315px; height: 453px; border: 1px solid var(--map-border); background: var(--map-fill); }

  .band--contact { left: 15px; top: 1064px; width: 895px; height: 107px; text-align: center; font-weight: 700; }
  .contact-line { margin-top: 14px; font-size: 26px; }
  .contact-line .phone { font-size: 33px; font-weight: 800; }
  .contact-line .soft { font-weight: 500; }
  .contact-email { display: inline-block; margin-top: 2px; font-size: 27px; border-bottom: 2px solid var(--paper); line-height: 32px; }
</style>
</head>
<body>
  <header class="band band--title"><h1>OFFICE SPACE FOR LEASE</h1></header>
  <p class="address">4867 W. TAMBERLIN AVENUE, LAUDERHILL, FL 33319</p>

  <div class="photo photo--main" role="img" aria-label="Photo of the white three-storey office building with parking lot in front"></div>

  <div class="band band--section band--info">BUILDING INFORMATION:</div>
  <ul class="facts">
    <li><span class="arrow"></span><span>Total Building Size: <b>42,040 SF</b></span></li>
    <li><span class="arrow"></span><span>Vacant Space: <b>38,000 SF</b></span></li>
    <li><span class="arrow"></span><span>1<sup>st</sup> and 2<sup>nd</sup> floor sizes: <b>about 15,500 each</b></span></li>
  </ul>

  <div class="photo photo--aerial" role="img" aria-label="Aerial photo of the building and its parking lot"></div>
  <div class="photo photo--street" role="img" aria-label="Street-level photo of the building front with landscaping"></div>

  <div class="band band--section band--marketing">MARKETING INFORMATION AND FEATURES:</div>
  <ul class="features">
    <li><span class="arrow"></span><span>New landlord purchased building recently and is moving into half of 3rd floor. Rest of building is vacant. New tenants can pick any location in the building they would like.</span></li>
    <li><span class="arrow"></span><span>Can accommodate a tenant up to 30,000 SF</span></li>
    <li><span class="arrow"></span><span>Monument signage available</span></li>
    <li><span class="arrow"></span><span>Located right on Tamberlin Avenue and a few blocks away from busiest intersection in all of Broward County of Tamberlin and US 441.</span></li>
    <li><span class="arrow"></span><span>Parking ratio over 5 per 1,000 SF including secured, private parking in rear of building.</span></li>
    <li><span class="arrow"></span><span>Building undergoing upgrades both exterior and interior:
      <ul class="sub">
        <li><span class="arrow"></span>New Landscaping</li>
        <li><span class="arrow"></span>New exterior paint</li>
        <li><span class="arrow"></span>Upgraded common area hallways</li>
        <li><span class="arrow"></span>Upgraded common area bathrooms</li>
        <li><span class="arrow"></span>New security card access system for building</li>
      </ul></span></li>
    <li><span class="arrow"></span><span>Negotiable tenant improvement allowances.</span></li>
    <li><span class="arrow"></span><span>Competitive rental rates.</span></li>
    <li><span class="arrow"></span><span>On-site management.</span></li>
    <li><span class="arrow"></span><span>Can accommodate professional or medical offices.</span></li>
  </ul>

  <div class="map" role="img" aria-label="Street map showing the building location in the neighbourhood"></div>

  <footer class="band band--contact">
    <p class="contact-line">Call Dana Whitlock <span class="soft">at</span> <span class="phone">561-555-0148</span> <span class="soft">or email</span></p>
    <span class="contact-email">dana@ordellholdings.com</span>
  </footer>
</body>
</html>
```